Design a BOLD Ad Design for Fitness Club

We are fitness facility that is about to run our new "Bright Parent Reboot" program and we need a bold design created for an ad that will run on Instagram and Facebook.

The ad needs to be eye catching, easy to read and attractive so that someone stops scrolling and clicks to join.

The add needs to be sized to 1080 x 1080, include our logo and the text "Bright Parent Reboot" and "Starting September 23rd"

I have included an example photo, which is to be used as an example only of a design style that stands out to us, (colors, female photo style, etc)

I have also included our logo, which the yellow color can be changed for this design.

Thank you and we look forward to seeing your design.

```html
<!DOCTYPE html>
<html lang="en">
<head>
<meta charset="utf-8">
<title>Bright Parent Reboot – Ad</title>
<link href="https://fonts.googleapis.com/css2?family=Bebas+Neue&family=Mr+Dafoe&family=Montserrat:wght@300;500;700&display=swap" rel="stylesheet">
<style>
  :root {
    --page: #a0a0a0;
    --ink: #0a0a0a;
    --ink-soft: #1c1c1c;
    --red: #d0172c;
    --red-deep: #8e0c1a;
    --white: #ffffff;
    --grey: #5a5a5a;
  }
  html, body {
    margin: 0; padding: 0;
    width: 1200px; height: 829px;
    overflow: hidden;
    background: var(--page);
  }
  .ad {
    position: absolute;
    left: 303px; top: 117px;
    width: 594px; height: 594px;
    overflow: hidden;
    background: radial-gradient(circle at 30% 55%, var(--ink-soft) 0%, var(--ink) 70%);
    font-family: "Montserrat", sans-serif;
    color: var(--white);
  }
  .ad__backdrop { position: absolute; inset: 0; }
  .ad__photo {
    position: absolute;
    left: 276px; top: 108px;
    width: 276px; height: 486px;
    background: radial-gradient(ellipse at 50% 40%, #c99a80 0%, #7a5448 40%, #3a2a34 75%, rgba(40,30,40,0) 100%);
    border-radius: 40% 40% 8% 8%;
  }
  .ad__title {
    position: absolute;
    left: 48px; top: 38px;
    margin: 0;
    font-family: "Bebas Neue", sans-serif;
    font-weight: 400;
    font-size: 86px;
    line-height: 1;
    letter-spacing: 1px;
    white-space: nowrap;
  }
  .ad__script {
    position: absolute;
    left: 44px; top: 108px;
    font-family: "Mr Dafoe", cursive;
    font-size: 82px;
    line-height: 1;
    color: var(--red);
  }
  .ad__dots { position: absolute; }
  .ad__chevrons { position: absolute; }
  .ad__starting {
    position: absolute;
    left: 59px; top: 226px;
    font-size: 17px;
    font-weight: 500;
    letter-spacing: 5px;
  }
  .ad__month {
    position: absolute;
    left: 49px; top: 256px;
    font-family: "Bebas Neue", sans-serif;
    font-size: 40px;
    line-height: 1;
    color: var(--red);
    letter-spacing: 0.5px;
  }
  .ad__datebox {
    position: absolute;
    left: 49px; top: 299px;
    width: 140px; height: 157px;
    border: 1px solid var(--red);
    box-sizing: border-box;
  }
  .ad__day {
    position: absolute;
    left: 0; right: 0; top: 2px;
    text-align: center;
    font-family: "Bebas Neue", sans-serif;
    font-size: 176px;
    line-height: 1;
  }
  .ad__year {
    position: absolute;
    left: 50%; top: 142px;
    transform: translateX(-50%);
    padding: 0 6px;
    background: var(--ink);
    font-size: 24px;
    font-weight: 300;
    letter-spacing: 6px;
    line-height: 1;
  }
  .ad__brand {
    position: absolute;
    left: 48px; top: 506px;
    width: 142px;
    text-align: center;
  }
  .ad__brand-name {
    display: flex; align-items: center; justify-content: center; gap: 6px;
    font-family: "Bebas Neue", sans-serif;
    font-size: 40px;
    line-height: 1;
    color: var(--white);
  }
  .ad__brand-mark {
    width: 12px; height: 12px;
    background: var(--red);
  }
  .ad__brand-tag {
    margin-top: 2px;
    font-size: 5.5px;
    font-weight: 700;
    letter-spacing: 0.8px;
    color: var(--red);
  }
  .ad__follow {
    position: absolute;
    left: 434px; top: 532px;
    display: flex; align-items: center; gap: 6px;
    font-size: 9px;
    font-weight: 500;
    letter-spacing: 1.5px;
  }
  .ad__follow-dot {
    width: 14px; height: 14px;
    border-radius: 50%;
    background: var(--red);
  }
</style>
</head>
<body>
  <main class="ad">
    <svg class="ad__backdrop" width="594" height="594" viewBox="0 0 594 594" aria-hidden="true">
      <defs>
        <linearGradient id="redPanel" x1="0" y1="0" x2="1" y2="1">
          <stop offset="0" stop-color="#e01a30"/>
          <stop offset="1" stop-color="#7d0a16"/>
        </linearGradient>
      </defs>
      <polygon points="594,20 520,140 462,243 380,360 276,489 198,594 594,594" fill="url(#redPanel)"/>
      <polygon points="0,0 140,0 110,8 40,12 0,10" fill="var(--red-deep)"/>
    </svg>

    <div class="ad__photo" role="img" aria-label="Smiling mother in sports top and leggings squatting while holding her baby"></div>

    <svg class="ad__dots" style="left:277px;top:14px" width="64" height="24" aria-hidden="true">
      <g fill="#fff">
        <circle cx="2" cy="2" r="1.5"/><circle cx="22" cy="2" r="1.5"/><circle cx="42" cy="2" r="1.5"/><circle cx="62" cy="2" r="1.5"/>
        <circle cx="2" cy="21" r="1.5"/><circle cx="22" cy="21" r="1.5"/><circle cx="42" cy="21" r="1.5"/><circle cx="62" cy="21" r="1.5"/>
      </g>
    </svg>
    <svg class="ad__dots" style="left:260px;top:229px" width="84" height="64" aria-hidden="true">
      <g fill="#fff">
        <circle cx="2" cy="2" r="1.5"/><circle cx="21" cy="2" r="1.5"/><circle cx="41" cy="2" r="1.5"/><circle cx="60" cy="2" r="1.5"/><circle cx="80" cy="2" r="1.5"/>
        <circle cx="2" cy="22" r="1.5"/><circle cx="21" cy="22" r="1.5"/><circle cx="41" cy="22" r="1.5"/><circle cx="60" cy="22" r="1.5"/><circle cx="80" cy="22" r="1.5"/>
        <circle cx="2" cy="42" r="1.5"/><circle cx="21" cy="42" r="1.5"/><circle cx="41" cy="42" r="1.5"/><circle cx="60" cy="42" r="1.5"/>
        <circle cx="2" cy="61" r="1.5"/><circle cx="21" cy="61" r="1.5"/><circle cx="41" cy="61" r="1.5"/>
      </g>
    </svg>

    <svg class="ad__chevrons" style="left:0;top:230px" width="38" height="14" aria-hidden="true">
      <g fill="var(--grey)">
        <polygon points="0,0 5,0 10,7 5,14 0,14 5,7"/>
        <polygon points="9,0 14,0 19,7 14,14 9,14 14,7"/>
        <polygon points="18,0 23,0 28,7 23,14 18,14 23,7"/>
        <polygon points="27,0 32,0 37,7 32,14 27,14 32,7"/>
      </g>
    </svg>
    <svg class="ad__chevrons" style="left:231px;top:420px" width="78" height="37" aria-hidden="true">
      <g fill="#3a3a3a">
        <polygon points="18,0 28,0 10,18.5 28,37 18,37 0,18.5"/>
        <polygon points="38,0 48,0 30,18.5 48,37 38,37 20,18.5"/>
        <polygon points="58,0 68,0 50,18.5 68,37 58,37 40,18.5"/>
      </g>
    </svg>

    <h1 class="ad__title">BRIGHT PARENT</h1>
    <div class="ad__script">Reboot</div>

    <div class="ad__starting">STARTING</div>
    <div class="ad__month">SEPTEMBER</div>
    <div class="ad__datebox">
      <div class="ad__day">23</div>
      <div class="ad__year">2024</div>
    </div>

    <div class="ad__brand">
      <div class="ad__brand-name"><span class="ad__brand-mark"></span>COREVIA</div>
      <div class="ad__brand-tag">PERSONAL GROUP TRAINING</div>
    </div>

    <div class="ad__follow">Follow us on <span class="ad__follow-dot"></span></div>
  </main>
</body>
</html>
```